DORIVAN
POWER THE FUTURE
Professional
Tobin Rasquelle
2417 Fennimore Lane
Alder Ridge, OH 44021
tobin@dorivan7.com
www.dorivan7.com
I can provide logo as need it.
Logo and write this underneath the logo or where you think it will look better.
Have fun!!

```html
<!DOCTYPE html>
<html lang="en">
<head>
<meta charset="utf-8">
<title>Dorivan Business Card</title>
<link href="https://fonts.googleapis.com/css2?family=Open+Sans:wght@400;600;700&display=swap" rel="stylesheet">
<style>
  :root {
    --brand-blue: #1f86d0;
    --brand-blue-deep: #1670b4;
    --card-white: #f7f8f9;
    --text-grey: #6b7177;
    --logo-grey: #8a9096;
    --rule-grey: #c9cdd1;
    --backdrop: #e9ebee;
  }
  * { box-sizing: border-box; margin: 0; padding: 0; }
  html, body {
    width: 1200px; height: 838px; overflow: hidden;
    background: var(--backdrop);
    font-family: "Open Sans", Arial, sans-serif;
  }
  .stage {
    width: 1200px; height: 838px;
    display: flex; align-items: center; justify-content: center; gap: 50px;
  }
  .card {
    position: relative;
    width: 540px; height: 309px;
    border-radius: 4px;
    overflow: hidden;
    box-shadow: 0 8px 24px rgba(0,0,0,0.18);
  }
  /* Front */
  .card-front { background: var(--card-white); }
  .front-band { position: absolute; top: 0; left: 0; width: 540px; height: 130px; }
  .brand {
    position: absolute; left: 0; right: 0; text-align: center;
    color: var(--logo-grey); font-weight: 700; letter-spacing: 2px;
  }
  .card-front .brand { top: 62px; font-size: 40px; line-height: 52px; }
  .tagline {
    position: absolute; left: 0; right: 0; text-align: center;
    font-size: 9px; letter-spacing: 4px; color: var(--logo-grey); font-weight: 600;
  }
  .card-front .tagline { top: 114px; }
  .holder-name {
    position: absolute; top: 138px; left: 0; right: 0; text-align: center;
    font-size: 27px; line-height: 38px; color: var(--brand-blue); font-weight: 400;
  }
  .name-rule {
    position: absolute; top: 184px; left: 60px; right: 60px;
    height: 1px; background: var(--rule-grey);
  }
  .contact {
    position: absolute; top: 196px; left: 60px; right: 60px;
    font-size: 12.5px; color: var(--text-grey); line-height: 24px;
  }
  .contact-row { display: flex; align-items: center; gap: 6px; white-space: nowrap; }
  .contact-row .sep { margin: 0 4px; color: var(--rule-grey); }
  .icon { width: 13px; height: 13px; flex: none; }
  /* Back */
  .card-back {
    background: linear-gradient(160deg, var(--brand-blue) 0%, var(--brand-blue-deep) 100%);
  }
  .card-back .brand { top: 110px; font-size: 52px; line-height: 66px; color: #e4e9ee; }
  .card-back .tagline { top: 180px; font-size: 11px; color: #d5e3f0; }
</style>
</head>
<body>
<main class="stage">
  <section class="card card-front">
    <svg class="front-band" viewBox="0 0 540 130" aria-hidden="true">
      <path d="M0 0 H540 V62 C400 40 160 30 0 78 Z" fill="var(--brand-blue)"/>
    </svg>
    <div class="brand">DORIVAN</div>
    <div class="tagline">POWER THE FUTURE</div>
    <h1 class="holder-name">Tobin Rasquelle</h1>
    <div class="name-rule"></div>
    <div class="contact">
      <div class="contact-row">
        <svg class="icon" viewBox="0 0 14 14"><path d="M7 1.5 L1 7 H3 V12.5 H11 V7 H13 Z" fill="var(--text-grey)"/></svg>
        <span>2417 Fennimore Lane, Alder Ridge, OH 44021</span>
      </div>
      <div class="contact-row">
        <svg class="icon" viewBox="0 0 14 14"><circle cx="7" cy="7" r="6" fill="none" stroke="var(--text-grey)" stroke-width="1.4"/><path d="M4.5 4 l1.5 0 l0.6 1.8 l-0.9 0.8 a5 5 0 0 0 1.8 1.8 l0.8 -0.9 l1.8 0.6 l0 1.5 a5 5 0 0 1 -5.6 -5.6z" fill="var(--text-grey)"/></svg>
        <span>1-800-555-0142</span><span class="sep">|</span>
        <svg class="icon" viewBox="0 0 14 14"><path d="M3 2 h3 l1 3 l-1.5 1.2 a7 7 0 0 0 3.3 3.3 l1.2 -1.5 l3 1 v3 a10 10 0 0 1 -10 -10z" fill="var(--text-grey)"/></svg>
        <span>412-555-0187</span><span class="sep">|</span>
        <svg class="icon" viewBox="0 0 14 14"><rect x="1" y="4" width="12" height="7" rx="1" fill="var(--text-grey)"/><rect x="3" y="1.5" width="8" height="3" fill="var(--text-grey)"/></svg>
        <span>412-555-0163</span>
      </div>
      <div class="contact-row">
        <svg class="icon" viewBox="0 0 14 14"><rect x="1" y="3" width="12" height="8" rx="1" fill="none" stroke="var(--text-grey)" stroke-width="1.4"/><path d="M1 3 L7 8 L13 3" fill="none" stroke="var(--text-grey)" stroke-width="1.4"/></svg>
        <span>tobin@dorivan7.com</span><span class="sep">|</span>
        <svg class="icon" viewBox="0 0 14 14"><circle cx="7" cy="7" r="6" fill="none" stroke="var(--text-grey)" stroke-width="1.3"/><ellipse cx="7" cy="7" rx="2.6" ry="6" fill="none" stroke="var(--text-grey)" stroke-width="1.1"/><path d="M1 7 H13" stroke="var(--text-grey)" stroke-width="1.1"/></svg>
        <span>www.dorivan7.com</span>
      </div>
    </div>
  </section>

  <section class="card card-back">
    <div class="brand">DORIVAN</div>
    <div class="tagline">POWER THE FUTURE</div>
  </section>
</main>
</body>
</html>
```